I need a design with just the number 24. must be in blue color (royal blue) should be large enough for people see must be in the center of page. Place a nice border around the page.

• Number 24 in Royal blue color

```html
<!DOCTYPE html>
<html lang="en">
<head>
<meta charset="UTF-8">
<title>House Number 24 – Design Options</title>
<link rel="stylesheet" href="https://fonts.googleapis.com/css2?family=Fraunces:opsz,wght@144,900&family=DM+Serif+Display&family=Caprasimo&family=Montserrat:wght@700&display=swap">
<style>
  :root {
    --royal-blue: #0000f2;
    --plate-white: #ffffff;
    --board-light: #cbcbcb;
    --board-dark: #a4a4a4;
    --label-white: #f4f4f4;
  }
  html, body {
    margin: 0;
    padding: 0;
    width: 1200px;
    height: 862px;
    overflow: hidden;
  }
  .board {
    position: relative;
    width: 1200px;
    height: 862px;
    background: radial-gradient(ellipse at 50% 45%, var(--board-light) 0%, var(--board-dark) 75%);
    font-family: "Montserrat", Arial, sans-serif;
  }
  .plate {
    position: absolute;
    width: 482px;
    height: 342px;
    background: var(--plate-white);
    overflow: hidden;
  }
  .plate--classic { left: 90px;  top: 42px; }
  .plate--serif   { left: 638px; top: 42px; }
  .plate--rounded { left: 372px; top: 424px; }

  .plate__frame {
    position: absolute;
    inset: 0;
    width: 482px;
    height: 342px;
  }
  .plate__number {
    position: absolute;
    inset: 0;
    display: flex;
    align-items: center;
    justify-content: center;
    color: var(--royal-blue);
    line-height: 1;
    font-variant-numeric: lining-nums;
    font-feature-settings: "lnum" 1;
  }
  .plate--classic .plate__number {
    font-family: "Fraunces", Georgia, serif;
    font-weight: 900;
    font-size: 300px;
    letter-spacing: -14px;
    padding-bottom: 18px;
  }
  .plate--serif .plate__number {
    font-family: "DM Serif Display", Georgia, serif;
    font-weight: 400;
    font-size: 330px;
    letter-spacing: -6px;
    padding-bottom: 24px;
  }
  .plate--rounded .plate__number {
    font-family: "Caprasimo", Georgia, serif;
    font-weight: 400;
    font-size: 300px;
    letter-spacing: -10px;
    padding-bottom: 16px;
  }
  .option-label {
    position: absolute;
    margin: 0;
    color: var(--label-white);
    font-weight: 700;
    font-size: 28px;
    letter-spacing: 0.5px;
    line-height: 1;
  }
  .option-label--1 { left: 88px;  top: 410px; }
  .option-label--2 { left: 921px; top: 404px; }
  .option-label--3 { left: 546px; top: 781px; }
</style>
</head>
<body>
<main class="board">

  <svg width="0" height="0" style="position:absolute">
    <defs>
      <g id="plate-border" fill="none" stroke="#0000f2">
        <rect x="10" y="10" width="462" height="322" stroke-width="4"/>
        <rect x="19" y="19" width="444" height="304" stroke-width="1.2"/>
        <g stroke-width="1.2">
          <rect x="14" y="14" width="16" height="16"/>
          <rect x="19" y="19" width="10" height="10"/>
          <rect x="452" y="14" width="16" height="16"/>
          <rect x="453" y="19" width="10" height="10"/>
          <rect x="14" y="312" width="16" height="16"/>
          <rect x="19" y="313" width="10" height="10"/>
          <rect x="452" y="312" width="16" height="16"/>
          <rect x="453" y="313" width="10" height="10"/>
        </g>
      </g>
    </defs>
  </svg>

  <section class="plate plate--classic">
    <svg class="plate__frame" viewBox="0 0 482 342"><use href="#plate-border"/></svg>
    <div class="plate__number">24</div>
  </section>
  <p class="option-label option-label--1">OPTION-1</p>

  <section class="plate plate--serif">
    <svg class="plate__frame" viewBox="0 0 482 342"><use href="#plate-border"/></svg>
    <div class="plate__number">24</div>
  </section>
  <p class="option-label option-label--2">OPTION-2</p>

  <section class="plate plate--rounded">
    <svg class="plate__frame" viewBox="0 0 482 342"><use href="#plate-border"/></svg>
    <div class="plate__number">24</div>
  </section>
  <p class="option-label option-label--3">OPTION-3</p>

</main>
</body>
</html>
```